Business Card Design

We recently had a new logo designed by Pixel Harbor. Now we want to create new business cards and letterhead that compliment our new logo.

We are audiologists in private practice specializing in hearing evaluations and fitting hearing aids. We want a clean and professional card.

We need business cards for each audiologist. The names and titles are:
Marnie Ostrova, AuD
Audiologist

Jen Tarbel, AuD
Audiologist

Corvina Plesk, AuD
Audiologist

We also need a business card with no provider. Just a generic one.

Finally, we need an appointment card. This is what the front desk uses to give to the patient with their next appointment date and time.

Target Market(s)

Our clients tend to be highly educated. They are older so the cards should be clean and easy to read. No squirrely font please.

Industry/Entity Type

Business

Contact Information for Business Card

20731 8th Ave NE, suite 417
Seattle, WA 98177
206-592-8074

Requirements
Must have
• Clean
Easy to read
Professional
Modern but approachable / warm
Should not have
• Other pictures besides the logo

```html
<!DOCTYPE html>
<html lang="en">
<head>
<meta charset="utf-8">
<title>Ridgeway Hearing Services – Business Cards</title>
<link href="https://fonts.googleapis.com/css2?family=Montserrat:wght@300;400;600&display=swap" rel="stylesheet">
<style>
  :root {
    --teal: #34aa97;
    --ink: #2b2b2b;
    --navy: #1f3f5c;
    --paper: #ffffff;
    --backdrop: #eeefee;
    --muted: #555555;
  }
  * { margin: 0; padding: 0; box-sizing: border-box; }
  html, body {
    width: 1200px; height: 900px; overflow: hidden;
    background: var(--backdrop);
    font-family: "Montserrat", Arial, sans-serif;
  }
  .stage { position: relative; width: 1200px; height: 900px; }
  .card {
    position: absolute; left: 300px; width: 600px; height: 342px;
    background: var(--paper);
    box-shadow: 3px 4px 6px rgba(0,0,0,0.28);
    overflow: hidden;
  }
  .card--front { top: 81px; }
  .card--back { top: 476px; }
  .band { position: absolute; left: 0; width: 100%; background: var(--teal); }
  .card--front .band--top { top: 0; height: 75px; }
  .card--front .band--bottom { bottom: 0; height: 75px; }
  .card--back .band--bottom { bottom: 0; height: 75px; }

  .brand { position: absolute; display: flex; align-items: center; gap: 10px; }
  .brand__dot { width: 34px; height: 34px; border-radius: 50%; background: var(--teal); flex: none; }
  .brand__name {
    color: var(--navy); font-weight: 600; font-size: 17px; line-height: 1.15;
    letter-spacing: 0.5px; width: 160px;
  }
  .card--front .brand { left: 200px; top: 140px; }
  .card--back .brand { left: 30px; top: 32px; }
  .card--back .brand__dot { width: 28px; height: 28px; }
  .card--back .brand__name { font-size: 15px; width: 140px; }

  .website {
    position: absolute; left: 0; right: 0; top: 296px; text-align: center;
    color: var(--paper); font-weight: 300; font-size: 13px; letter-spacing: 3px;
  }
  .provider { position: absolute; right: 50px; top: 212px; text-align: right; }
  .provider__name { color: var(--ink); font-weight: 400; font-size: 23px; letter-spacing: 0.3px; line-height: 1.1; }
  .provider__title { color: var(--muted); font-weight: 400; font-size: 11.5px; margin-top: 1px; }
  .contact {
    position: absolute; right: 50px; top: 275px; text-align: right;
    color: var(--paper); font-weight: 300; font-size: 12px; line-height: 19.5px;
  }
</style>
</head>
<body>
<main class="stage">
  <section class="card card--front">
    <div class="band band--top"></div>
    <div class="brand">
      <span class="brand__dot"></span>
      <span class="brand__name">Ridgeway Hearing Services</span>
    </div>
    <div class="band band--bottom"></div>
    <p class="website">www.ridgewayhearing.com</p>
  </section>

  <section class="card card--back">
    <div class="brand">
      <span class="brand__dot"></span>
      <span class="brand__name">Ridgeway Hearing Services</span>
    </div>
    <div class="provider">
      <p class="provider__name">MARNIE OSTROVA, AuD</p>
      <p class="provider__title">Audiologist</p>
    </div>
    <div class="band band--bottom"></div>
    <address class="contact" style="font-style:normal">
      206-592-8074<br>
      20731 8th Avenue NE, suite 417<br>
      Seattle, WA 98177
    </address>
  </section>
</main>
</body>
</html>
```